Conceptual Model Diagram for Replacing Medication with Behavior to Support Weight Loss Maintenance

Design a figure of a conceptual model that needs to be inserted into a word document for a PSF grant. This conceptual model illustrates how behavioral strategies can replace the regulatory functions lost after AOM discontinuation. The intervention targets three core vulnerabilities—appetite resurgence, metabolic inflexibility, and suboptimal mindstate—through the domains of Food, Physical Activity, and Mind. Sustained weight loss maintenance occurs at the intersection of these domains. The intervention is delivered within a design framework that makes behaviors easier to perform, aligns them with identity, and reinforces them through virtual support and community, ensuring real-world feasibility and long-term adherence.
Target Market(s)
PSF reviewers
Industry/Entity Type
academic
Other font styles liked:
- arial
Requirements
Must have
- see my attached description

```html
<!DOCTYPE html>
<html lang="en">
<head>
<meta charset="utf-8">
<title>Conceptual Model: Behavior-Based Weight Loss Maintenance</title>
<link rel="stylesheet" href="https://fonts.googleapis.com/css2?family=Inter:wght@500;600;700&display=swap">
<style>
  :root {
    --ink: #2f3a3c;
    --paper: #ffffff;
  }
  html, body {
    margin: 0;
    padding: 0;
    width: 1200px;
    height: 808px;
    overflow: hidden;
    background: var(--paper);
  }
  .model {
    display: block;
    width: 1200px;
    height: 808px;
    font-family: "Inter", Arial, sans-serif;
  }
  .box { fill: var(--paper); stroke: var(--ink); stroke-width: 4; }
  .domain { fill: none; stroke: var(--ink); stroke-width: 3.5; }
  .arrow { fill: var(--ink); }
  .loop { fill: none; stroke: var(--ink); stroke-width: 46; stroke-linecap: butt; }
  .label { fill: var(--ink); text-anchor: middle; }
  .label-box { font-size: 50px; font-weight: 600; }
  .label-domain { font-size: 72px; font-weight: 600; }
  .label-domain-center { font-size: 52px; font-weight: 600; }
  .label-core { font-size: 60px; font-weight: 700; }
  .label-framework { font-size: 62px; font-weight: 600; }
  .core-clear { fill: var(--paper); }
</style>
</head>
<body>
<svg class="model" viewBox="0 0 2330 1567" preserveAspectRatio="none" role="img" aria-label="Conceptual model: three vulnerabilities feed into the Food, Physical Activity and Mind domains, which meet at sustained weight loss maintenance, within a design framework">

  <g class="vulnerabilities">
    <rect class="box" x="353" y="84" width="412" height="170" rx="18"/>
    <text class="label label-box" x="559" y="158">Appetite</text>
    <text class="label label-box" x="559" y="218">Resurgence</text>

    <rect class="box" x="820" y="84" width="578" height="170" rx="18"/>
    <text class="label label-box" x="1109" y="182">Metabolic Inflexibility</text>

    <rect class="box" x="1455" y="84" width="480" height="170" rx="18"/>
    <text class="label label-box" x="1688" y="158">Suboptimal</text>
    <text class="label label-box" x="1688" y="218">Mindstate</text>
  </g>

  <g class="down-arrows">
    <polygon class="arrow" points="545,254 588,254 588,330 612,330 565,374 518,330 545,330"/>
    <polygon class="arrow" points="1100,254 1145,254 1145,330 1167,330 1122,374 1077,330 1100,330"/>
    <polygon class="arrow" points="1670,254 1713,254 1713,330 1738,330 1690,374 1645,330 1670,330"/>
  </g>

  <g class="domains">
    <circle class="domain" cx="782" cy="655" r="280"/>
    <circle class="domain" cx="1127" cy="655" r="280"/>
    <circle class="domain" cx="1480" cy="655" r="280"/>
    <rect class="core-clear" x="932" y="462" width="390" height="345"/>
    <text class="label label-domain" x="690" y="670">Food</text>
    <text class="label label-domain" x="1575" y="670">Mind</text>
    <text class="label label-domain-center" x="1127" y="510">Physical</text>
    <text class="label label-domain-center" x="1127" y="568">Activity</text>
    <text class="label label-core" x="1127" y="662">Sustained</text>
    <text class="label label-core" x="1127" y="726">Weight Loss</text>
    <text class="label label-core" x="1127" y="790">Maintenance</text>
  </g>

  <g class="framework-loop">
    <path class="loop" d="M 505,848 C 420,920 380,980 380,1050 C 380,1250 740,1393 1130,1393 C 1520,1393 1882,1250 1882,1050 C 1882,980 1842,920 1755,848"/>
    <polygon class="arrow" points="537,814 520,886 468,830"/>
    <polygon class="arrow" points="1722,814 1794,830 1740,886"/>
  </g>

  <g class="principles">
    <rect class="box" x="485" y="972" width="340" height="171" rx="18"/>
    <text class="label label-box" x="660" y="1045">Make It</text>
    <text class="label label-box" x="660" y="1105">Easy</text>

    <rect class="box" x="912" y="972" width="478" height="171" rx="18"/>
    <text class="label label-box" x="1140" y="1045">Make It</text>
    <text class="label label-box" x="1140" y="1105">Identity-Aligned</text>

    <rect class="box" x="1476" y="972" width="314" height="171" rx="18"/>
    <text class="label label-box" x="1630" y="1045">Make It</text>
    <text class="label label-box" x="1630" y="1105">Supported</text>
  </g>

  <text class="label label-framework" x="1125" y="1240">Design Framework</text>
</svg>
</body>
</html>
```